Business cards for financial advisor-insurance agent firm

Our company, Marlowe Pettigrew Insurance & Investments, is an insurance (health, life, home, auto, etc) and investment brokerage offering a suite of options to meet client needs. We need business cards that are professional and embody strength, security and sophistication.

Also running a letterhead project at
http://briefs.artboardhub.com/brief.aspx?id=517962

Target Market(s)

Upper middle class and wealthy

Industry/Entity Type

Investment

Requirements
Nice to have
• Looking for either white, navy blue, or gray cards

```html
<!DOCTYPE html>
<html lang="en">
<head>
<meta charset="utf-8">
<title>Marlowe Pettigrew Insurance &amp; Investments – Business Cards</title>
<link href="https://fonts.googleapis.com/css2?family=Cormorant+Garamond:wght@500&family=Courier+Prime&display=swap" rel="stylesheet">
<style>
  :root {
    --stage: #d9d9db;
    --navy: #3f4566;
    --navy-light: #525a7c;
    --navy-dark: #343a58;
    --paper: #ffffff;
    --ink: #2c3150;
    --name-tint: #93a2bb;
  }
  * { margin: 0; padding: 0; box-sizing: border-box; }
  html, body { width: 1200px; height: 750px; overflow: hidden; }
  body {
    background: var(--stage);
    position: relative;
    font-family: "Cormorant Garamond", serif;
  }
  .card {
    position: absolute;
    top: 232px;
    width: 500px;
    height: 286px;
    border-radius: 22px;
    overflow: hidden;
    box-shadow: 0 6px 18px rgba(0,0,0,0.18);
  }
  .card--details { left: 60px; }
  .card--brand {
    left: 640px;
    background: linear-gradient(135deg, var(--navy-light), var(--navy-dark));
    display: flex;
    align-items: center;
    justify-content: center;
  }
  .card__shape { position: absolute; inset: 0; }

  .company-name {
    display: flex;
    flex-direction: column;
    align-items: center;
    text-align: center;
    color: var(--name-tint);
    font-weight: 500;
  }
  .company-name__title { font-size: 30px; line-height: 1.1; }
  .company-name__line { font-size: 15px; margin-top: 4px; }

  .details { position: absolute; inset: 0; color: var(--ink); }
  .details .company-name {
    position: absolute;
    top: 40px; left: 187px; width: 240px;
    color: var(--ink);
  }
  .details .company-name__title { font-size: 17px; }
  .details .company-name__line { font-size: 10px; margin-top: 1px; }
  .contact {
    position: absolute;
    top: 112px; left: 150px;
    font-family: "Courier Prime", monospace;
    font-size: 12px;
    line-height: 1.35;
    list-style: none;
  }
</style>
</head>
<body>

  <section class="card card--details" aria-label="Business card, contact side">
    <svg class="card__shape" viewBox="0 0 500 286" aria-hidden="true">
      <rect width="500" height="286" fill="var(--navy)"/>
      <circle cx="307" cy="177" r="212" fill="var(--paper)"/>
    </svg>
    <div class="details">
      <div class="company-name">
        <span class="company-name__title">Marlowe Pettigrew</span>
        <span class="company-name__line">Insurance &amp; Investments</span>
      </div>
      <ul class="contact">
        <li>More details goes here</li>
        <li>Name : Evan Hale</li>
        <li>Email : marlowepettigrew@example.com</li>
        <li>Phone : 0012345855</li>
        <li>Adress : adress here</li>
        <li>Website : www.marlowepettigrew.com</li>
      </ul>
    </div>
  </section>

  <section class="card card--brand" aria-label="Business card, brand side">
    <div class="company-name">
      <span class="company-name__title">Marlowe Pettigrew</span>
      <span class="company-name__line">Insurance &amp; Investments</span>
    </div>
  </section>

</body>
</html>
```